Bramwell Hydraulics & Engineering Ute and Toolbox Wrap

Design a utility vehicle wrap (partial or full) and toolbox wrap for the attached vehicle images. Pink area on image files shows coverage.
The client offers hydraulic and engineering services.
Files in uploads.
https://www.bramwellhydraulics.example.au/

Target Market(s)

Mostly men, people who work with machinery

Industry/Entity Type

Engineering

```html
<!DOCTYPE html>
<html lang="en">
<head>
<meta charset="utf-8">
<title>Bramwell Hydraulics &amp; Engineering – Ute and Toolbox Wrap</title>
<link rel="stylesheet" href="https://fonts.googleapis.com/css2?family=Russo+One&family=Montserrat:wght@500&display=swap">
<style>
  :root {
    --wrap-red: #b0202c;
    --body-red: #a81d27;
    --navy: #1e3366;
    --white: #ffffff;
    --steel-light: #d9dde2;
    --steel-dark: #6d737b;
    --backdrop: #eceef1;
  }
  * { margin: 0; padding: 0; box-sizing: border-box; }
  html, body { width: 1200px; height: 620px; overflow: hidden; background: var(--backdrop); }
  .canvas { position: relative; width: 1200px; height: 620px; }

  /* Toolbox wrap */
  .toolbox-wrap {
    position: absolute; left: 40px; top: 190px; width: 460px; height: 210px;
    box-shadow: 0 4px 14px rgba(0,0,0,.15);
  }
  .toolbox-wrap svg.toolbox-bg { position: absolute; inset: 0; }
  .brand-lockup {
    position: absolute; left: 30px; top: 50px; display: flex; align-items: center; gap: 10px;
  }
  .brand-mark { width: 22px; height: 22px; background: var(--navy); }
  .brand-name {
    font-family: "Russo One", sans-serif; color: var(--navy); line-height: 1.05;
  }
  .brand-name .primary { display: block; font-size: 20px; letter-spacing: .5px; }
  .brand-name .secondary { display: block; font-size: 9.5px; letter-spacing: 1.2px; }
  .toolbox-latch {
    position: absolute; left: 96px; top: 150px; width: 42px; height: 34px;
    border: 3px solid var(--steel-dark); border-radius: 4px; background: var(--steel-light);
  }
  .phone {
    position: absolute; left: 240px; top: 66px; font-family: "Russo One", sans-serif;
    font-size: 21px; color: var(--white); letter-spacing: .5px;
  }
  .web-band {
    position: absolute; left: 240px; top: 115px; font-family: "Montserrat", sans-serif;
    font-weight: 500; font-size: 10px; color: var(--white);
  }

  /* Door wrap */
  .door-wrap {
    position: absolute; left: 540px; top: 90px; width: 620px; height: 440px;
    background: var(--body-red); box-shadow: 0 4px 14px rgba(0,0,0,.15); overflow: hidden;
  }
  .door-wrap svg.brush { position: absolute; inset: 0; }
  .fittings-photo {
    position: absolute; left: 28px; top: 210px; width: 240px; height: 205px;
    background: linear-gradient(90deg, #cfd3d8 0%, #9aa0a7 45%, #2a2a2e 70%, #141416 100%);
    border-radius: 6px;
  }
  .slogan {
    position: absolute; left: 270px; top: 282px; width: 290px; text-align: center;
    font-family: "Russo One", sans-serif; font-size: 19px; line-height: 1.35;
    color: var(--white); letter-spacing: .6px;
  }
</style>
</head>
<body>
<main class="canvas">

  <section class="toolbox-wrap" aria-label="Toolbox wrap">
    <svg class="toolbox-bg" width="460" height="210" viewBox="0 0 460 210">
      <rect width="460" height="210" fill="var(--white)"/>
      <polygon points="195,0 460,0 460,210 245,210" fill="var(--wrap-red)"/>
      <polygon points="205,102 460,102 460,138 215,138" fill="var(--navy)"/>
    </svg>
    <div class="brand-lockup">
      <span class="brand-mark"></span>
      <span class="brand-name">
        <span class="primary">BRAMWELL</span>
        <span class="secondary">HYDRAULICS &amp; ENGINEERING</span>
      </span>
    </div>
    <div class="toolbox-latch"></div>
    <div class="phone">(07) 4000 2681</div>
    <div class="web-band">www.bramwellhydraulics.example.au</div>
  </section>

  <section class="door-wrap" aria-label="Door wrap">
    <svg class="brush" width="620" height="440" viewBox="0 0 620 440">
      <polygon fill="var(--white)" points="300,235 545,195 560,225 550,240 600,258 572,275 590,300 560,322 596,345 560,365 580,392 520,410 560,430 360,440 350,430 545,420 500,405 560,385 540,365 575,345 548,322 578,300 555,278 585,260 540,244 548,225 535,205"/>
      <polygon fill="var(--navy)" points="300,228 320,220 470,200 540,192 552,215 538,232 585,252 555,270 575,295 545,318 580,340 545,362 566,388 500,408 540,425 250,440 265,420 245,405 262,385 240,360 260,340 245,320 262,298 240,275 268,252 255,238"/>
    </svg>
    <div class="fittings-photo" role="img" aria-label="Photo of chrome hydraulic hose fittings crimped onto black hoses"></div>
    <p class="slogan">COMBINING<br>INNOVATION WITH<br>PRECISION &amp; QUALITY</p>
  </section>

</main>
</body>
</html>
```